Startup fashion company needs high-end, stylish and hip business cards!

We need a business card design that uses a logo that we just completed with a SketchHive artist.

Our company is Velmora. We work with fashion designers to display their designs on our website and handle all back-end fulfillment for them (fabric sourcing, garment manufacturing, customer service, etc.). The word Velmora is a play on fashion trunk shows, where designers will show their wares in a small, intimate setting. The final design should communicate high-end / luxe, chic, stylish, fashion-forward, hip!

We are using greys as our logo color (#2d2d2d, #ababab). We are also interested, for branding purposes and on our website, to use purple as a highlight color (#4a3455). I have the logo in other formats if needed.

Target Market(s)

Investors, customers, fashion designers, suppliers

Industry/Entity Type

Fashion

Contact Information for Business Card

There should be space for:
Name
Title
Address 1
Address 2
City, State Zip
USA
Phone
Email
Chatly
Chirper

If it makes sense to put one or more of the contact info on the same line, that is fine if it won't be confusing.

Font styles to use
Sans Serif
Other font styles liked:
• Would like the font to be complementary to our logo font/look and feel. The logo font is Caviar Dreams with a stylized 'N' according to the logo designer.

Colors
876aae
e4daea
f3f1f8
ffffff

Requirements
Must have
• The cards will most likely printed through PrintNova and therefore must meet their upload file guidelines. There are also software templates for business cards that can be utilized. Information below from PrintNova site.
• We support a variety of file formats for uploaded designs.
• Adobe Acrobat 9 Document (*.pdf) (recommended)
• Adobe Illustrator CS3 Artwork (*.ai) (recommended)
• Adobe Photoshop CS3 Image (*.psd) (recommended)
• Bitmap Image (*.bmp)
• GIF Image (*.gif)
• JPEG Image (*.jpg,*.jpeg)
• Microsoft PowerPoint 2010 Document (*.ppt)
• Microsoft Publisher 2010 Document (*.pub)
• Microsoft Word 2010 Document (*.doc)
• PCX Image (*.pcx)
• PICT Image (*.pic,*.pict,*.pct)
• PNG Image (*.png)
• PostScript Document (*.ps)
• TIFF Image (*.tif,*.tiff)
• Windows Enhanced Metafile (*.emf)
• Windows Metafile (*.wmf)
• The templates on their site:
• Using a downloadable template for your application will ensure that your dimensions, resolution and color settings match ours.
• If you are creating a PDF document in Acrobat Distiller, please use our Distiller settings.
• Sizing:
• Full Bleed Size
• 3.62" x 2.12"
• 92 x 54 mm
• 1085 x 635 pixels
• Document Trim Size
• 3.50" x 2.00"
• 89 x 51 mm
• 1050 x 600 pixels
Nice to have
• The back can use either the full logo or just the elephant or a combination? I'm imagining a full color backside...open to other suggestions!

```html
<!DOCTYPE html>
<html lang="en">
<head>
<meta charset="utf-8">
<title>Velmora Business Card</title>
<link rel="stylesheet" href="https://fonts.googleapis.com/css2?family=Questrial&family=Didact+Gothic&display=swap">
<style>
  :root {
    --page-bg: #e9e6ec;
    --ink-dark: #2d2d2d;
    --brand-purple: #876aae;
    --brand-purple-light: #a68acb;
    --brand-deep: #4a3455;
    --lavender: #e4daea;
    --lavender-pale: #f3f1f8;
    --white: #ffffff;
  }
  * { box-sizing: border-box; margin: 0; padding: 0; }
  html, body { width: 1200px; height: 885px; overflow: hidden; }
  body {
    background: var(--page-bg);
    font-family: "Didact Gothic", "Questrial", sans-serif;
    display: flex;
    flex-direction: column;
    align-items: center;
    justify-content: center;
    gap: 32px;
  }
  .card {
    width: 700px;
    height: 400px;
    position: relative;
    overflow: hidden;
    box-shadow: 0 6px 18px rgba(45, 45, 45, 0.18);
  }

  /* Front */
  .card-front { background: var(--white); display: flex; flex-direction: column; }
  .brand-area {
    height: 178px;
    display: flex;
    align-items: center;
    padding: 0 0 0 90px;
  }
  .brand-block {
    display: inline-flex;
    flex-direction: column;
    align-items: flex-end;
  }
  .brand-line { display: flex; align-items: center; gap: 12px; }
  .brand-dot {
    width: 54px; height: 54px; border-radius: 50%;
    background: var(--brand-deep);
  }
  .brand-name {
    font-family: "Didact Gothic", sans-serif;
    font-size: 66px;
    letter-spacing: 3px;
    color: var(--ink-dark);
    line-height: 1;
  }
  .brand-email {
    margin-top: 10px;
    font-size: 19px;
    color: var(--ink-dark);
    letter-spacing: 0.5px;
  }
  .info-band {
    flex: 1;
    background: linear-gradient(100deg, var(--brand-purple-light) 0%, var(--brand-purple) 70%, #7a5ea2 100%);
    color: var(--white);
    display: flex;
    align-items: center;
    padding: 0 40px 0 44px;
  }
  .person { width: 300px; }
  .person-name { font-family: "Questrial", sans-serif; font-weight: 700; font-size: 27px; letter-spacing: 0.5px; }
  .person-title { font-size: 20px; margin-top: 2px; }
  .person-address { font-size: 17px; margin-top: 14px; line-height: 1.35; }
  .divider {
    width: 1px; height: 150px;
    background: rgba(255, 255, 255, 0.75);
    margin: 0 36px 0 20px;
  }
  .contact-list { list-style: none; font-size: 17px; line-height: 1.9; }
  .contact-list li { display: flex; align-items: center; gap: 10px; }
  .contact-icon {
    width: 17px; height: 17px; border-radius: 3px;
    background: var(--white);
    display: flex; align-items: center; justify-content: center;
    flex-shrink: 0;
  }
  .contact-icon svg { width: 12px; height: 12px; }

  /* Back */
  .card-back {
    background: radial-gradient(ellipse at 40% 30%, var(--white) 0%, var(--lavender-pale) 45%, var(--lavender) 100%);
    display: flex;
    align-items: center;
    justify-content: center;
    gap: 18px;
  }
  .back-dot {
    width: 70px; height: 70px; border-radius: 50%;
    background: var(--brand-purple-light);
  }
  .back-name {
    font-family: "Didact Gothic", sans-serif;
    font-size: 72px;
    letter-spacing: 4px;
    color: var(--brand-purple-light);
  }
</style>
</head>
<body>
  <section class="card card-front">
    <div class="brand-area">
      <div class="brand-block">
        <div class="brand-line">
          <span class="brand-dot"></span>
          <span class="brand-name">VELMORA</span>
        </div>
        <div class="brand-email">info@youremail.com</div>
      </div>
    </div>
    <div class="info-band">
      <div class="person">
        <div class="person-name">Employee Name</div>
        <div class="person-title">Managing Director</div>
        <div class="person-address">Your Adress Inc 2nd Lane<br>Ave Edison, NJ 00000</div>
      </div>
      <div class="divider"></div>
      <ul class="contact-list">
        <li>
          <span class="contact-icon">
            <svg viewBox="0 0 12 12"><path d="M3 1 L4.6 3.6 L3.6 4.6 Q4.6 6.9 7.4 8.4 L8.4 7.4 L11 9 L10 11 Q4 10.5 1 2 Z" fill="#876aae"/></svg>
          </span>0012 3456 789
        </li>
        <li><span class="contact-icon"></span>Your Chatly Address</li>
        <li><span class="contact-icon"></span>Your Chirper Address</li>
        <li>
          <span class="contact-icon">
            <svg viewBox="0 0 12 12"><path d="M6 11 Q2 6.5 2 4.5 A4 4 0 0 1 10 4.5 Q10 6.5 6 11 Z" fill="#876aae"/><circle cx="6" cy="4.5" r="1.5" fill="#ffffff"/></svg>
          </span>City, State Zip USA
        </li>
      </ul>
    </div>
  </section>

  <section class="card card-back">
    <span class="back-dot"></span>
    <span class="back-name">VELMORA</span>
  </section>
</body>
</html>
```